Personal Finance Blog Wordpress Design

We are looking for a new Wordpress theme design for CoinHarborly.com.

All of the elements that are currently on the homepage should remain, minus the archives list. The placement of various elements can be changed, we just need a more modern and clean feel. We would like to add a 160 x 600 ad unit on the homepage. We would like the 728x90 ad to be below the navigation similar to that of: http://www.plumtreeledger.org/blog/

We like the fonts used on: http://www.quillpocket.com/blog/

The text that currently resides at the bottom of CoinHarborly.com needs to remain on the homepage, but wherever it is placed needs to not be intrusive.

The color scheme needs to appropriately compliment the logo.

No sliders. I don't like sliders.

I am happy to answer questions.

Industry/Entity Type

Finance

Requirements
Must have
• Included in project description
Nice to have
Should not have
• Included in project description. Don't use sliders

```html
<!DOCTYPE html>
<html lang="en">
<head>
<meta charset="utf-8">
<title>CoinHarborly — Personal Finance Blog</title>
<link href="https://fonts.googleapis.com/css2?family=Open+Sans:wght@400;600;700&family=Noto+Serif:wght@400;700&display=swap" rel="stylesheet">
<style>
:root{
  --green:#5b9c1f;
  --green-dark:#3f7412;
  --green-light:#8cc43c;
  --ink:#2d2d2d;
  --muted:#6c6c6c;
  --line:#dcdcdc;
  --band:#ececec;
  --footer:#262626;
  --paper:#ffffff;
  --orange:#f29b1d;
}
*{box-sizing:border-box;margin:0;padding:0}
html,body{width:784px;height:1200px;overflow:hidden;background:var(--paper)}
body{font-family:"Open Sans",sans-serif;color:var(--ink);font-size:9px;line-height:1.35;position:relative}

/* header */
.site-header{position:absolute;left:0;top:0;width:784px;height:56px;display:flex;align-items:center;justify-content:space-between;padding:0 24px 0 20px}
.brand{display:flex;align-items:center;gap:8px}
.brand-mark{width:26px;height:26px;border-radius:50%;background:var(--green)}
.brand-name{font-size:22px;font-weight:700;color:var(--green-dark);letter-spacing:-.3px}
.call{display:flex;align-items:center;gap:8px}
.call-icon{width:28px;height:28px;border-radius:50%;background:var(--green);display:flex;align-items:center;justify-content:center}
.call small{display:block;font-size:8px;color:var(--muted);font-weight:600;letter-spacing:.5px}
.call strong{font-size:19px;color:var(--green-dark);font-weight:700;line-height:1}

/* nav */
.main-nav{position:absolute;left:0;top:56px;width:784px;height:27px;background:var(--green);display:flex;align-items:center;padding-left:20px;border-bottom:3px solid var(--green-dark)}
.main-nav a{color:#fff;text-decoration:none;font-size:8.5px;font-weight:700;padding:0 10px;line-height:24px;letter-spacing:.2px}
.main-nav a.active{background:var(--green-light);border-radius:2px;padding:0 8px;margin-right:4px}

/* ads */
.ad-sky{position:absolute;left:14px;top:95px;width:124px;height:440px;background:linear-gradient(180deg,#f6f6f6 0%,#e7eef0 55%,#c9d6dc 100%);border:1px solid var(--line)}
.ad-sky .tag{position:absolute;left:0;top:0;width:100%;height:58px;background:var(--green);color:#fff;font-weight:700;font-size:12px;text-align:center;padding-top:10px;line-height:1.25}
.ad-sky .art{position:absolute;left:10px;top:80px;width:102px;height:80px;background:linear-gradient(180deg,#c43b2e,#8e2219);border-radius:6px}
.ad-leader{position:absolute;left:222px;top:95px;width:548px;height:44px;background:linear-gradient(90deg,#f4c838 0%,#f0b21e 60%,#e6a514 100%)}
.ad-leader .msg{position:absolute;left:72px;top:8px;width:190px;height:28px;background:var(--green-dark);color:#fff;font-weight:700;font-size:11px;text-align:center;line-height:1.2;padding-top:2px}
.ad-leader .house{position:absolute;left:6px;top:4px;width:58px;height:36px;background:linear-gradient(180deg,#e9f1f6,#bcd0dc)}
.ad-leader .btn{position:absolute;right:70px;top:7px;width:100px;height:30px;background:var(--green);color:#fff;font-weight:700;font-size:10px;text-align:center;line-height:1.2;padding-top:3px;border-radius:3px}

/* news */
.section-title{font-family:"Noto Serif",serif;font-weight:700;font-size:20px;color:var(--ink);text-align:center;letter-spacing:.5px}
.news-title{position:absolute;left:150px;top:150px;width:620px}
.news-main{position:absolute;left:150px;top:185px;width:300px}
.news-item{display:flex;gap:10px;padding-bottom:14px;margin-bottom:14px;border-bottom:1px solid var(--line)}
.thumb{flex:none;background:linear-gradient(135deg,#d8e8c6,#8bb85a)}
.news-item .thumb{width:102px;height:78px}
.news-item h3{font-family:"Noto Serif",serif;font-size:11px;font-weight:700;line-height:1.25;margin-bottom:3px}
.news-item p{color:var(--muted);font-size:8.5px}
.meta{font-size:7.5px;color:var(--green-dark);font-weight:600;margin-top:4px}
.news-side{position:absolute;left:470px;top:185px;width:300px}
.side-item{display:flex;gap:8px;padding-bottom:10px;margin-bottom:10px;border-bottom:1px solid var(--line)}
.side-item .thumb{width:70px;height:52px}
.side-item h4{font-family:"Noto Serif",serif;font-size:10px;font-weight:700;line-height:1.25;margin-bottom:2px}
.side-item p{font-size:8px;color:var(--muted)}

/* services */
.services{position:absolute;left:0;top:558px;width:784px;height:405px;background:var(--band)}
.services .section-title{position:absolute;left:0;top:32px;width:784px;font-size:21px}
.rule{position:absolute;left:362px;top:66px;width:60px;height:2px;background:var(--green)}
.cards{position:absolute;left:38px;top:88px;width:708px;display:flex;gap:12px}
.card{width:168px;background:var(--paper);height:300px;position:relative}
.card-tab{height:24px;background:var(--green);color:#fff;font-weight:700;font-size:10px;line-height:24px;padding-left:10px;letter-spacing:.3px}
.card-tab.dark{background:var(--green-dark)}
.card-body{padding:8px 8px 0}
.card h3{font-family:"Noto Serif",serif;font-size:10.5px;font-weight:700;line-height:1.25;height:40px;margin-bottom:6px}
.card .thumb{width:152px;height:82px;margin-bottom:7px}
.card p{font-size:8px;color:var(--muted);height:62px;overflow:hidden}
.card ul{list-style:none;border-top:1px solid var(--line);padding-top:5px;margin-top:6px}
.card li{font-size:7.8px;color:var(--green-dark);line-height:1.4;padding-left:8px;position:relative}
.card li::before{content:"";position:absolute;left:0;top:4px;width:3px;height:3px;background:var(--green)}

/* about */
.about{position:absolute;left:20px;top:978px;width:520px}
.about h2{font-family:"Noto Serif",serif;font-size:15px;font-weight:700;color:var(--green-dark);margin-bottom:6px}
.about p{font-size:8px;color:var(--muted);line-height:1.45;margin-bottom:5px}
.ad-box{position:absolute;left:552px;top:982px;width:218px;height:104px;border:1px solid var(--line);background:linear-gradient(180deg,#ffffff,#eef5e6)}
.ad-box .amount{position:absolute;left:12px;top:30px;font-size:20px;font-weight:700;color:var(--green-dark)}
.ad-box .small{position:absolute;left:12px;top:14px;font-size:9px;color:var(--muted);font-weight:600}
.ad-box .go{position:absolute;left:12px;top:66px;width:80px;height:22px;background:var(--orange);color:#fff;font-weight:700;font-size:9px;text-align:center;line-height:22px;border-radius:2px}
.ad-box .art{position:absolute;right:10px;top:14px;width:90px;height:76px;background:linear-gradient(135deg,#dfeecb,#9bc86a)}

/* newsletter */
.newsletter{position:absolute;left:0;top:1104px;width:784px;height:46px;background:var(--green);display:flex;align-items:center;padding:0 20px;gap:12px}
.newsletter .mail{width:30px;height:30px;border-radius:50%;background:var(--green-dark);display:flex;align-items:center;justify-content:center}
.newsletter .copy strong{display:block;color:#fff;font-size:11px;font-weight:700;letter-spacing:.3px}
.newsletter .copy span{color:#e4f2d2;font-size:7.5px}
.newsletter .field{margin-left:auto;width:250px;height:22px;background:#fff;border-radius:2px;font-size:8px;color:#999;line-height:22px;padding-left:8px}
.newsletter .submit{width:64px;height:22px;background:var(--green-dark);color:#fff;font-size:9px;font-weight:700;text-align:center;line-height:22px;border-radius:2px}

/* footer */
.site-footer{position:absolute;left:0;top:1150px;width:784px;height:50px;background:var(--footer);color:#bdbdbd;font-size:8px;display:flex;align-items:center;justify-content:center;gap:4px}
.site-footer a{color:#bdbdbd;text-decoration:none}
</style>
</head>
<body>

<header class="site-header">
  <div class="brand"><span class="brand-mark"></span><span class="brand-name">CoinHarborly</span></div>
  <div class="call">
    <span class="call-icon"><svg width="14" height="14" viewBox="0 0 24 24"><path fill="#fff" d="M6.6 10.8a15.1 15.1 0 0 0 6.6 6.6l2.2-2.2c.3-.3.7-.4 1-.2 1.1.4 2.3.6 3.6.6.6 0 1 .4 1 1V20c0 .6-.4 1-1 1A17 17 0 0 1 3 4c0-.6.4-1 1-1h3.5c.6 0 1 .4 1 1 0 1.3.2 2.5.6 3.6.1.3 0 .7-.2 1z"/></svg></span>
    <div><small>CALL US NOW!</small><strong>020-555-0147</strong></div>
  </div>
</header>

<nav class="main-nav">
  <a class="active">HOME</a><a>BANK ACCOUNTS</a><a>CREDIT CARDS</a><a>FINANCE</a><a>INVESTMENTS</a><a>MORTGAGES</a><a>PERSONAL FINANCE</a><a>SMALL BUSINESS</a><a>TAXES</a>
</nav>

<aside class="ad-sky" role="img" aria-label="Skyscraper advertisement with a red car photo">
  <div class="tag">Sell Your Old Car<br>at Good Price</div>
  <div class="art"></div>
</aside>

<div class="ad-leader" role="img" aria-label="Leaderboard advertisement for house rentals with a house photo">
  <div class="house"></div>
  <div class="msg">RENT A HOUSE IN<br>LARKMOOR</div>
  <div class="btn">LOOK UP<br>HOUSING</div>
</div>

<h2 class="section-title news-title">NEWS UPDATES</h2>

<section class="news-main">
  <article class="news-item">
    <div class="thumb" role="img" aria-label="Home financing promo photo"></div>
    <div>
      <h3>NestTrail Financing</h3>
      <p>How It Helps First-Time Homebuyers. This housing market is one of the most important indicators of the economy in the United States, and buyers feel it first.</p>
      <div class="meta">Apr 26th, 2013 · 0 Comments</div>
    </div>
  </article>
  <article class="news-item">
    <div class="thumb" role="img" aria-label="House for sale photo"></div>
    <div>
      <h3>Important Tips about Short Sales Every Home Buyer Should Know</h3>
      <p>You have heard that short sales are a great deal, yet they carry risks that every careful buyer should weigh.</p>
      <div class="meta">Apr 26th, 2013 · 0 Comments</div>
    </div>
  </article>
  <article class="news-item">
    <div class="thumb" role="img" aria-label="Home financing promo photo"></div>
    <div>
      <h3>NestTrail Financing</h3>
      <p>How It Helps First-Time Homebuyers. The housing market is one of the most important indicators of the economy, and many people have turned to this option.</p>
      <div class="meta">Apr 26th, 2013 · 0 Comments</div>
    </div>
  </article>
</section>

<section class="news-side">
  <article class="side-item">
    <div class="thumb" role="img" aria-label="Shopping coupons photo"></div>
    <div><h4>Best Coupon Apps for the Frugal Mom</h4><p>It can be hard to juggle the bills, but a few handy apps make saving simple.</p><div class="meta">Apr 26th, 2013</div></div>
  </article>
  <article class="side-item">
    <div class="thumb" role="img" aria-label="Person working at laptop photo"></div>
    <div><h4>Real Work from Home Jobs: Fact or Fiction?</h4><p>Many people dream of working from home, but which offers are real?</p><div class="meta">Apr 26th, 2013</div></div>
  </article>
  <article class="side-item">
    <div class="thumb" role="img" aria-label="House for sale photo"></div>
    <div><h4>Important Tips about Short Sales Every Home Buyer Should Know</h4><p>Short sales can save money when you know the steps.</p><div class="meta">Apr 26th, 2013</div></div>
  </article>
  <article class="side-item">
    <div class="thumb" role="img" aria-label="House and keys photo"></div>
    <div><h4>How To Home Loan Interest Rates Work For You?</h4><p>With mortgage interest rates at record lows, now may be the time.</p><div class="meta">Apr 26th, 2013</div></div>
  </article>
</section>

<section class="services">
  <h2 class="section-title">OUR SERVICES</h2>
  <span class="rule"></span>
  <div class="cards">
    <article class="card">
      <div class="card-tab">AUTO</div>
      <div class="card-body">
        <h3>Car Shopping on Budget? Costs Car Buying in a Given Option</h3>
        <div class="thumb" role="img" aria-label="New car photo"></div>
        <p>Many consumers are currently trying to find a new vehicle and want to make sure they get the best deal. Some people need a reliable car.</p>
        <ul><li>Credit Tips for Students: How to Get Credit</li><li>How to Qualify for a Discount Student Loan</li></ul>
      </div>
    </article>
    <article class="card">
      <div class="card-tab dark">BANK ACCOUNTS</div>
      <div class="card-body">
        <h3>Want to Increase Your Savings? Check Out These Saving Tips</h3>
        <div class="thumb" role="img" aria-label="Piggy bank and coins photo"></div>
        <p>Increasing the amount of money in a savings account is a good choice for every family that wants to stay secure.</p>
        <ul><li>Five Ways To Obtain Affordable Car Insurance</li><li>How to Protect Yourself From Insurance Fraud</li></ul>
      </div>
    </article>
    <article class="card">
      <div class="card-tab">CREDIT CARDS</div>
      <div class="card-body">
        <h3>Benefits of a Harborline Card with Cash Back</h3>
        <div class="thumb" role="img" aria-label="Credit cards photo"></div>
        <p>The card company was founded a few decades ago and has since become a well known name among everyday shoppers.</p>
        <ul><li>Are 401 Overlimit Savings Worth Missing Out?</li><li>Average Retirement Savings Needed by Retiree</li></ul>
      </div>
    </article>
    <article class="card">
      <div class="card-tab dark">INSURANCE</div>
      <div class="card-body">
        <h3>What is the Best Dental Insurance for Seniors?</h3>
        <div class="thumb" role="img" aria-label="Senior couple photo"></div>
        <p>No matter what your age, your dental health is important. Seniors often find it hard to find dental cover they can trust.</p>
        <ul><li>Important Tips About Short Sales Every Buyer Should Know</li><li>How To Home Loan Interest Rates Work for You?</li></ul>
      </div>
    </article>
  </div>
</section>

<section class="about">
  <h2>CoinHarborly: Personal Finance Blog</h2>
  <p>Our mission is to enrich the lives of our readers. We do this by providing the very best personal finance content on the internet. Our readers may be at different stages in life, with different personal finance situations and needs. Our goal is to help them find clear answers and simple steps they can trust.</p>
  <p>Whether you are looking for ways to save on groceries, pay down credit card debt, build an emergency fund, compare bank accounts, or plan for retirement, you will find practical guides and honest reviews here. We believe good money habits grow over time.</p>
  <p>We cover credit cards, bank accounts, insurance, investments and taxes, and we update our articles often so readers always have current numbers. Thank you for reading and for sharing our work with friends.</p>
</section>

<div class="ad-box" role="img" aria-label="Loan advertisement with a family photo">
  <span class="small">Get up to</span>
  <span class="amount">$35,000</span>
  <span class="go">See Rates</span>
  <div class="art"></div>
</div>

<section class="newsletter">
  <span class="mail"><svg width="16" height="12" viewBox="0 0 16 12"><rect x="1" y="1" width="14" height="10" fill="none" stroke="#fff" stroke-width="1.5"/><path d="m1 1 7 6 7-6" fill="none" stroke="#fff" stroke-width="1.5"/></svg></span>
  <div class="copy"><strong>E-MAIL NEWSLETTER</strong><span>Sign up now to receive breaking news and to hear what's new with us first.</span></div>
  <div class="field">Enter your email address</div>
  <div class="submit">SUBMIT</div>
</section>

<footer class="site-footer">
  <span>© 2013 CoinHarborly. All right reserved.</span><span>|</span><a>Contact Us</a><span>|</span><a>Privacy Policy</a><span>|</span><a>Terms and Conditions</a>
</footer>

</body>
</html>
```